Cover for "TANDEM! The skill and rhythm of guiding teams through calm and delight"

My first book for a global audience of modern performance leaders needs its cover!
I am an international executive coach and I've developed a new approach to replace classic Performance Management with a natural, sustainable approach fit for human beings :) My first book is about this approach and serves two purposes: helping leaders and sparking their curiosity to learn more, and positioning myself as a thought leader in the field.
The book is built on personal experience; it is both professional and personal ("From me to You"), and I'd like to position it beyond classic categorisation.
Its cover should communicate humanness, naturalness, ease and joy, within an unmistakably business-y context. I would like to see designs that use the color yellow (but not sure it communicates the right things).
Updates

Sick

Target Market(s)

Leaders who aspire to have a positive impact and deliver results in a meaningful way

Industry/Entity Type

Consulting & Executive Coaching - Trusted Advisor

Font styles to use
Other font styles liked:
• Helvetica Neue

Colors
0094D4
00A9DD
6FCCEA
C7EBF8
E9F6FB
FFC000
F8CF3A
FAE287
FDF2CF
FEFAEE
EE7325
F08F49
F5BC92
FAE3D3
FDF4ED

Requirements
Must have
• A both-and feeling to it (see description), e.g., masculine AND feminine, business AND humanness. Power with, not power over...
Should not have
• Too much "bling" - no classic status symbol business success language

```html
<!DOCTYPE html>
<html lang="en">
<head>
<meta charset="utf-8">
<title>TANDEM! — Book Cover</title>
<link href="https://fonts.googleapis.com/css2?family=Bebas+Neue&display=swap" rel="stylesheet">
<style>
  :root {
    --paper: #ffffff;
    --navy: #062a40;
    --berry: #c0427a;
    --tone-yellow: #fbe6a0;
    --tone-pink: #f6c3d8;
    --tone-teal: #bfe9e8;
    --tone-blue: #c9dcf2;
  }
  html, body {
    margin: 0;
    padding: 0;
    width: 802px;
    height: 1200px;
    overflow: hidden;
    background: var(--paper);
  }
  .cover {
    position: relative;
    width: 802px;
    height: 1200px;
    background: var(--paper);
    font-family: "Bebas Neue", "Arial Narrow", sans-serif;
  }
  .cover__subtitle {
    position: absolute;
    top: 62px;
    left: 0;
    width: 100%;
    margin: 0;
    text-align: center;
    color: var(--berry);
    font-family: "Bebas Neue", "Arial Narrow", sans-serif;
    font-weight: 400;
    font-size: 44px;
    line-height: 41px;
    letter-spacing: 0.5px;
  }
  .cover__title {
    position: absolute;
    top: 150px;
    left: 48px;
    width: 709px;
    height: 290px;
    margin: 0;
  }
  .cover__title text {
    fill: var(--navy);
    font-family: "Bebas Neue", "Arial Narrow", sans-serif;
    font-size: 398px;
  }
  .cover__illustration {
    position: absolute;
    top: 452px;
    left: 0;
    width: 802px;
    height: 526px;
    background:
      radial-gradient(ellipse at 35% 70%, var(--tone-pink) 0%, rgba(246,195,216,0) 45%),
      radial-gradient(ellipse at 55% 40%, var(--tone-yellow) 0%, rgba(251,230,160,0) 50%),
      radial-gradient(ellipse at 72% 62%, var(--tone-blue) 0%, rgba(201,220,242,0) 45%),
      radial-gradient(ellipse at 50% 75%, var(--tone-teal) 0%, rgba(191,233,232,0) 55%),
      var(--paper);
  }
  .cover__author-band {
    position: absolute;
    top: 1066px;
    left: 0;
    width: 802px;
    height: 72px;
    background: var(--navy);
    display: flex;
    align-items: center;
    justify-content: center;
  }
  .cover__author {
    margin: 0;
    color: var(--paper);
    font-family: "Bebas Neue", "Arial Narrow", sans-serif;
    font-size: 48px;
    line-height: 1;
    letter-spacing: 0.5px;
    padding-top: 6px;
  }
</style>
</head>
<body>
  <main class="cover">
    <p class="cover__subtitle">The skill and rhythm of guiding<br>teams through calm and delight</p>

    <h1 class="cover__title" aria-label="TANDEM!">
      <svg width="709" height="290" viewBox="0 0 709 290" aria-hidden="true">
        <text x="0" y="285" textLength="709" lengthAdjust="spacingAndGlyphs">TANDEM!</text>
      </svg>
    </h1>

    <div class="cover__illustration" role="img"
         aria-label="Illustration of a team climbing colourful rising bar blocks with ladders, reaching for yellow stars, with paper planes and a light bulb"></div>

    <div class="cover__author-band">
      <p class="cover__author">Author Name</p>
    </div>
  </main>
</body>
</html>
```